Existing App Needs A Facelift

The Vellix Kneader is an existing mobile application that needs an update. I built this way before the zephone 8 or 5s as well as ZenOS 4 came out so there is obvious room for improvement. You can find the app here https://appmart.example-store.net/us/app/vellix-kneader/id804415261?mt=8 and see the creative direction it needs to go. I need a new appcon that reflects the ZenOS 4 design structure.

You can download the PSD files from here :
https://www.filecrate-share.net/sh/t7rw42pzq1dmxbn/HvaroLKEWT

Colors

Designer to choose colors to be used in the design.

Requirements
Must have
• It must have the hand-held massager.

```html
<!DOCTYPE html>
<html lang="en">
<head>
<meta charset="utf-8">
<title>Vellix Kneader – App Screens</title>
<link href="https://fonts.googleapis.com/css2?family=Open+Sans:wght@600;700;800&family=Arimo:wght@400&display=swap" rel="stylesheet">
<style>
  :root{
    --page:#ffffff;
    --ink-dark:#2d2a37;
    --list-bg:#333040;
    --divider:#26232f;
    --red:#df4a55;
    --red-deep:#c62630;
    --tile:#161616;
    --label-grey:#c9c9cc;
    --white:#ffffff;
    --picker-ink:#111111;
    --picker-fade:#9a9a9a;
    --picker-faint:#c4c4c4;
  }
  *{box-sizing:border-box;margin:0;padding:0}
  html,body{width:1200px;height:900px;overflow:hidden;background:var(--page)}
  body{position:relative;font-family:"Open Sans",Arial,sans-serif}

  .screen{position:absolute;top:30px;width:475px;height:843px;background:var(--ink-dark);overflow:hidden}
  .screen--share{left:93px}
  .screen--timer{left:633px}

  .status-bar{position:absolute;top:0;left:0;right:0;height:30px;color:var(--white);font-family:"Arimo",Arial,sans-serif;font-size:16px;display:flex;align-items:center;padding:0 10px}
  .status-bar .signal{letter-spacing:-1px;margin-right:4px}
  .status-bar .time{position:absolute;left:0;right:0;text-align:center}
  .status-bar .right{margin-left:auto;display:flex;align-items:center;gap:5px}
  .battery{width:34px;height:14px;border:1.5px solid var(--white);border-radius:3px;padding:1px;position:relative}
  .battery::before{content:"";display:block;height:100%;background:var(--white);border-radius:1px}
  .battery::after{content:"";position:absolute;right:-4px;top:3px;width:2px;height:5px;background:var(--white)}

  .app-header{position:absolute;top:30px;left:0;right:0;height:100px;background:var(--red);border-top:14px solid var(--red-deep);border-radius:8px 8px 0 0;box-shadow:0 6px 10px rgba(0,0,0,.35);display:flex;align-items:center;justify-content:center;z-index:2}
  .app-title{color:var(--white);font-weight:800;font-size:29px;letter-spacing:.5px;margin-top:-2px}

  .intro-panel{position:absolute;top:130px;left:0;right:0;height:153px;background:var(--ink-dark)}
  .share-list{position:absolute;top:283px;left:0;right:0;list-style:none}
  .share-item{height:150px;background:var(--list-bg);border-bottom:1px solid var(--divider);position:relative;display:flex;align-items:center}
  .share-tile{position:absolute;left:30px;top:29px;width:92px;height:92px;background:var(--tile);box-shadow:inset 0 0 0 3px #222;display:flex;align-items:center;justify-content:center}
  .share-label{position:absolute;left:164px;color:var(--label-grey);font-weight:700;font-size:27px}
  .share-chevron{position:absolute;right:46px;top:60px}

  .section-title{position:absolute;top:132px;left:0;right:0;height:88px;display:flex;align-items:center;justify-content:center;color:var(--white);font-weight:600;font-size:24px;letter-spacing:.3px}
  .time-picker{position:absolute;top:220px;left:0;right:0;height:262px;background:var(--white);border-top:1px solid #555;font-family:"Arimo",Arial,sans-serif;overflow:hidden}
  .picker-row{position:absolute;left:0;right:0;height:40px;line-height:40px;color:var(--picker-fade)}
  .picker-row span{position:absolute;top:0}
  .col-day{right:263px;text-align:right}
  .col-hour{left:254px;transform:translateX(-50%)}
  .col-min{left:339px;transform:translateX(-50%)}
  .col-ampm{left:393px}
  .picker-row--faint{color:var(--picker-faint);font-size:21px;transform:scaleY(.62)}
  .picker-row--mid{font-size:24px;color:#a8a8a8;transform:scaleY(.88)}
  .picker-row--near{font-size:27px}
  .picker-row--selected{color:var(--picker-ink);font-size:32px;top:105px;height:51px;line-height:51px;border-top:1.5px solid #aaa;border-bottom:1.5px solid #aaa}
  .set-timer{position:absolute;left:36px;top:553px;width:400px;height:114px;border-radius:10px;background:linear-gradient(#ffffff,#d9d9dc);box-shadow:0 4px 6px rgba(0,0,0,.5);display:flex;align-items:center;justify-content:center;color:var(--red);font-weight:800;font-size:50px;border:none;font-family:inherit}

  .tab-bar{position:absolute;bottom:0;left:4px;right:4px;height:107px;display:flex}
  .tab{background:var(--red);display:flex;flex-direction:column;align-items:center;justify-content:center;color:var(--white);font-weight:600;font-size:13px;gap:8px;box-shadow:inset -6px 0 8px -6px rgba(0,0,0,.35)}
  .tab svg{height:44px}
  .tab--intensity{width:96px}
  .tab--timer{width:102px}
  .tab--music{width:93px}
  .tab--share{width:93px;background:var(--ink-dark);box-shadow:none}
  .tab--next{width:84px}
</style>
</head>
<body>

<section class="screen screen--share">
  <div class="status-bar"><span class="signal">●●●●○</span> Carrier <span class="time">12:34 AM</span><span class="right">➤ ✱ 100% <span class="battery"></span></span></div>
  <header class="app-header"><h1 class="app-title">VELLIX KNEADER</h1></header>
  <div class="intro-panel"></div>
  <ul class="share-list">
    <li class="share-item"><span class="share-tile"></span><span class="share-label">FRIENDLOOP</span>
      <svg class="share-chevron" width="22" height="30" viewBox="0 0 22 30"><path d="M2 1l18 14L2 29" fill="none" stroke="#55525f" stroke-width="2"/></svg></li>
    <li class="share-item"><span class="share-tile"></span><span class="share-label">CHIRPLINE</span>
      <svg class="share-chevron" width="22" height="30" viewBox="0 0 22 30"><path d="M2 1l18 14L2 29" fill="none" stroke="#55525f" stroke-width="2"/></svg></li>
    <li class="share-item"><span class="share-tile">
      <svg width="42" height="32" viewBox="0 0 42 32"><rect x="2" y="2" width="38" height="28" rx="3" fill="none" stroke="#fff" stroke-width="3"/><path d="M3 4l18 14L39 4" fill="none" stroke="#fff" stroke-width="3"/></svg></span>
      <span class="share-label">EMAIL</span>
      <svg class="share-chevron" width="22" height="30" viewBox="0 0 22 30"><path d="M2 1l18 14L2 29" fill="none" stroke="#55525f" stroke-width="2"/></svg></li>
  </ul>
  <nav class="tab-bar">
    <div class="tab tab--intensity"><svg role="img" aria-label="Hand icon" viewBox="0 0 40 44" width="40"><rect x="8" y="14" width="24" height="26" rx="10" fill="#fff"/><rect x="8" y="4" width="5" height="18" rx="2.5" fill="#fff"/><rect x="15" y="1" width="5" height="18" rx="2.5" fill="#fff"/><rect x="22" y="2" width="5" height="18" rx="2.5" fill="#fff"/><rect x="29" y="6" width="5" height="18" rx="2.5" fill="#fff"/></svg>Intensity</div>
    <div class="tab tab--timer"><svg viewBox="0 0 44 44" width="44"><circle cx="22" cy="22" r="18" fill="none" stroke="#fff" stroke-width="4"/><path d="M22 11v12h9" fill="none" stroke="#fff" stroke-width="4"/></svg>Timer</div>
    <div class="tab tab--music"><svg viewBox="0 0 40 44" width="40"><path d="M14 8l20-5v28" fill="none" stroke="#fff" stroke-width="4"/><path d="M14 8v28" stroke="#fff" stroke-width="4"/><ellipse cx="9" cy="36" rx="7" ry="5.5" fill="#fff"/><ellipse cx="29" cy="31" rx="7" ry="5.5" fill="#fff"/></svg>Music</div>
    <div class="tab tab--share"><svg viewBox="0 0 48 44" width="48"><path d="M6 16v22h28v-8" fill="none" stroke="#cfcfd4" stroke-width="4"/><path d="M14 30c0-12 8-17 20-17V6l12 11-12 11v-7c-9 0-15 3-20 9z" fill="#cfcfd4"/></svg>Share</div>
    <div class="tab tab--next"><svg viewBox="0 0 30 44" width="30"><path d="M6 6l16 16L6 38" fill="none" stroke="#fff" stroke-width="7"/></svg></div>
  </nav>
</section>

<section class="screen screen--timer">
  <div class="status-bar"><span class="signal">●●●●○</span> Carrier <span class="time">12:34 AM</span><span class="right">➤ ✱ 100% <span class="battery"></span></span></div>
  <header class="app-header"><h1 class="app-title">VELLIX KNEADER</h1></header>
  <h2 class="section-title">SELECT A TIME</h2>
  <div class="time-picker">
    <div class="picker-row picker-row--faint" style="top:-5px"><span class="col-day">Thu Jun 27</span><span class="col-hour">6</span><span class="col-min">57</span></div>
    <div class="picker-row picker-row--mid" style="top:25px"><span class="col-day">Fri Jun 28</span><span class="col-hour">7</span><span class="col-min">58</span></div>
    <div class="picker-row picker-row--near" style="top:65px"><span class="col-day">Sat Jun 30</span><span class="col-hour">8</span><span class="col-min">59</span></div>
    <div class="picker-row picker-row--selected"><span class="col-day">Today</span><span class="col-hour">9</span><span class="col-min">00</span><span class="col-ampm">AM</span></div>
    <div class="picker-row picker-row--near" style="top:158px"><span class="col-day">Tue Jul 2</span><span class="col-hour">10</span><span class="col-min">01</span><span class="col-ampm">PM</span></div>
    <div class="picker-row picker-row--mid" style="top:198px"><span class="col-day">Wed Jul 3</span><span class="col-hour">11</span><span class="col-min">02</span></div>
    <div class="picker-row picker-row--faint" style="top:226px"><span class="col-day">Thu Jul 4</span><span class="col-hour">12</span><span class="col-min">03</span></div>
  </div>
  <button class="set-timer">SET TIMER</button>
  <nav class="tab-bar">
    <div class="tab tab--intensity"><svg role="img" aria-label="Hand icon" viewBox="0 0 40 44" width="40"><rect x="8" y="14" width="24" height="26" rx="10" fill="#fff"/><rect x="8" y="4" width="5" height="18" rx="2.5" fill="#fff"/><rect x="15" y="1" width="5" height="18" rx="2.5" fill="#fff"/><rect x="22" y="2" width="5" height="18" rx="2.5" fill="#fff"/><rect x="29" y="6" width="5" height="18" rx="2.5" fill="#fff"/></svg>Intensity</div>
    <div class="tab tab--timer"><svg viewBox="0 0 44 44" width="44"><circle cx="22" cy="22" r="18" fill="none" stroke="#fff" stroke-width="4"/><path d="M22 11v12h9" fill="none" stroke="#fff" stroke-width="4"/></svg>Timer</div>
    <div class="tab tab--music"><svg viewBox="0 0 40 44" width="40"><path d="M14 8l20-5v28" fill="none" stroke="#fff" stroke-width="4"/><path d="M14 8v28" stroke="#fff" stroke-width="4"/><ellipse cx="9" cy="36" rx="7" ry="5.5" fill="#fff"/><ellipse cx="29" cy="31" rx="7" ry="5.5" fill="#fff"/></svg>Music</div>
    <div class="tab tab--share"><svg viewBox="0 0 48 44" width="48"><path d="M6 16v22h28v-8" fill="none" stroke="#cfcfd4" stroke-width="4"/><path d="M14 30c0-12 8-17 20-17V6l12 11-12 11v-7c-9 0-15 3-20 9z" fill="#cfcfd4"/></svg>Share</div>
    <div class="tab tab--next"><svg viewBox="0 0 30 44" width="30"><path d="M6 6l16 16L6 38" fill="none" stroke="#fff" stroke-width="7"/></svg></div>
  </nav>
</section>

</body>
</html>
```